Velvet Crest Car Detailing Brochure

I would like a trifold brochure designed for my car detailing business. The background has to be full black or mostly black with some designing using only colors present in our logo.

Front page must have our logo and name, list of services, a photo and mybe our phone number but no long text.

Inside I want to present each service one by one with its description and a photo representing/showing each service. (I will provide the text below). For photos, use stock photos and I will add come of mines already too.

On the back of the brochure I want to have contact & info: phone number, opening hours, address, website, Instagram.

Outside left I want the text About us and photo/design.

I want the brochure to be neat, professional, easy to read, but at the same time not too boring.

Text:
1. About us
a. the ultimate destination for car care in Geneva. We provide personalized, detail-oriented services that bring out the best in your car. With our expert techniques and dedicated approach, we ensure that your car receives the utmost care and attention. Experience a place where passion meets precision and let us create an exceptional car care experience designed just for you.
2. Services:

DETAILING & HAND WASH

• Comprehensive exterior & interior care
• Personalisation and tailored cleaning packages
• Decontamination
• Premium products
• Attention to detail for a perfect finish

POLISHING

• Eliminates scratches, holograms
• Revives and protects paint
• Ensures lasting gloss
• Enhances paint life
• Preserves car’s value and beauty

CERAMIC TREATMENT

• Durable paint protection
• Water-repellent (hydrophobic) effect
• Easier cleaning, enhanced shine
• Long-term surface safeguarding
• Shields against environmental impacts

DRY ICE WASH

• Innovative, waterless method
• Safe for all car parts
• Deep cleans, removes odors
• Allergen-free, antibacterial
• Gentle, effective
• Advanced cleaning technology

COVERING

• Personalized vehicle styling
• More than 150 colours available
• Clean cut without using a cutter
• High-quality, durable materials
• Custom designs available

PROTECTION FILM

• Invisible, durable shield
• Self-healing technology
• 10-year warranty by QR VONT

DETAILING BOUTIQUE

• Premium brands available
• Buy on site during your visit
• Marble Harbour, Zeb Autos, DRUP Polaro
• Essential for at-home car care
• Perfect for quick touch-ups
(for these three brands you can put their logos

Target Market(s)

Our target market includes car owners of all price ranges, with a special focus on those who are passionate about their vehicles. We cater to clients who value excellent service and results, and seek to maintain their cars in pristine condition.

Industry/Entity Type

Automobile / Car detailing

Colors

Designer to choose colors to be used in the design.

Requirements
Must have
• Brand Consistency: The brochure must adhere to our brand colors and style, particularly utilizing the colors present in our logo. Trifold Layout: The design must be specifically tailored for a trifold brochure format. Legibility: Text must be easy to read against the mostly black background, with appropriate font size and style. Professional Look and Feel: The overall design must convey professionalism while being engaging and not overly complex. Photo representation: each service description should have a phot presenting it.
Should not have
• Overcrowded Design: Avoid cluttering with too much text or too many images. The layout should be clean and easy to navigate. Cartoonish Fonts or Graphics: Avoid using unprofessional or casual fonts and graphics that do not align with the upscale and professional image of our business. Distracting Backgrounds: The background should complement and not overpower the content. Stick to the theme of mostly black with design elements from our logo.

```html
<!DOCTYPE html>
<html lang="en">
<head>
<meta charset="utf-8">
<title>Velvet Crest Car Detailing – Trifold Brochure</title>
<link href="https://fonts.googleapis.com/css2?family=Open+Sans:ital,wght@0,400;0,600;0,700;1,400&display=swap" rel="stylesheet">
<style>
  :root{
    --ink:#000;
    --paper:#fff;
    --stage:#e4e4e7;
    --blue:#4a90dc;
    --violet:#8a6ccf;
    --pink:#dc4396;
    --brand-grad:linear-gradient(90deg,var(--blue),var(--violet) 50%,var(--pink));
  }
  *{box-sizing:border-box;margin:0;padding:0}
  html,body{width:922px;height:1200px;overflow:hidden}
  body{background:var(--stage);font-family:"Open Sans",Arial,sans-serif;color:var(--paper);position:relative}

  .sheet{position:absolute;left:63px;width:796px;height:562px;background:var(--ink);overflow:hidden}
  .sheet--outside{top:30px}
  .sheet--inside{top:608px}

  /* three folded panels of each side, 265px wide */
  .panel{position:absolute;top:0;height:562px}
  .panel--flap{left:0;width:265px}
  .panel--back{left:265px;width:266px}
  .panel--front{left:531px;width:265px}

  .abs{position:absolute}
  .photo{position:absolute}

  /* outside: photo runs across inner flap and back panel */
  .cover-art{position:absolute;left:0;top:0}
  .back-name{position:absolute;left:133px;top:233px;transform:translate(-50%,-50%);font-size:17px;font-weight:700;letter-spacing:1px;text-align:center;line-height:1.15}
  .back-contact{position:absolute;left:33px;width:200px;top:467px;text-align:center;font-size:13.5px;line-height:18.5px}
  .front-name{position:absolute;left:-8px;width:160px;top:203px;text-align:center;font-size:21px;line-height:25px;letter-spacing:.5px}
  .front-services{position:absolute;right:58px;top:348px;text-align:right;font-style:italic;font-size:13px;line-height:17px;text-transform:uppercase}
  .front-phone{position:absolute;left:72px;width:160px;top:490px;text-align:center;font-size:19px;font-weight:700}

  /* inside */
  .services-band{left:163px;top:36px;width:368px;height:59px;background:var(--brand-grad);font-size:38px;font-weight:700;line-height:59px;padding-left:118px;letter-spacing:.3px}
  .service-title{font-size:17px;letter-spacing:.3px;line-height:20px;white-space:nowrap}
  .grad-text{background:var(--brand-grad);-webkit-background-clip:text;background-clip:text;color:transparent}
  .bullets{list-style:none;font-size:9px;line-height:11.4px}
  .bullets li::before{content:"• "}
  .label-box{left:266px;top:281px;width:130px;height:30px;background:var(--paper);color:var(--ink);font-size:17px;line-height:30px;padding-left:16px}
  .covering-band{left:531px;top:173px;width:165px;height:33px;background:var(--brand-grad);font-size:17px;line-height:33px;padding-left:26px}
  .ceramic-box{left:266px;top:440px;width:265px;height:105px;background:linear-gradient(90deg,var(--blue),var(--violet) 45%,var(--pink));padding:8px 0 0 16px}
  .about-title{left:24px;top:260px;font-size:36px;font-weight:700;letter-spacing:.5px}
  .about-text{left:24px;top:329px;width:222px;font-size:8.9px;line-height:11.4px}
  .white-bar{background:var(--paper)}
</style>
</head>
<body>

<!-- Outside: inner flap, back panel, front cover -->
<section class="sheet sheet--outside" aria-label="Brochure outside">
  <svg class="cover-art" width="796" height="562" viewBox="0 0 796 562">
    <defs>
      <linearGradient id="panelGrad" x1="0" y1="0" x2="0" y2="562" gradientUnits="userSpaceOnUse">
        <stop offset="0" stop-color="#4a90dc"/>
        <stop offset=".45" stop-color="#8a6ccf"/>
        <stop offset="1" stop-color="#dc4396"/>
      </linearGradient>
      <linearGradient id="photoGrad" x1="0" y1="0" x2="1" y2="1">
        <stop offset="0" stop-color="#3a3a3d"/>
        <stop offset=".5" stop-color="#2c2c2e"/>
        <stop offset="1" stop-color="#232325"/>
      </linearGradient>
    </defs>
    <rect x="0" y="0" width="531" height="562" fill="url(#photoGrad)" role="img" aria-label="Photo of a technician dry ice washing a car, steam rising, dark toned"/>
    <rect x="531" y="0" width="265" height="562" fill="url(#panelGrad)"/>
    <path d="M531,38 C640,34 735,60 752,130 C768,200 700,250 640,290 C560,340 492,380 496,430 C500,480 620,520 720,562 L531,562 Z" fill="#000"/>
    <path d="M752,130 C768,200 700,250 640,290 C560,340 492,380 496,430 C500,480 620,520 720,562 L796,562 L796,130 Z" fill="url(#panelGrad)"/>
    <path d="M700,250 C770,305 790,405 758,452 C728,488 620,486 516,472" fill="none" stroke="#fff" stroke-width="2"/>
    <circle cx="398" cy="233" r="70" fill="none" stroke="#8a6ccf" stroke-width="3"/>
    <circle cx="603" cy="146" r="50" fill="none" stroke="#8a6ccf" stroke-width="3"/>
  </svg>

  <div class="panel panel--flap"></div>

  <div class="panel panel--back">
    <div class="back-name">VELVET<br>CREST</div>
    <div class="back-contact">131313 24 680<br>hello@velvetcrest.ch<br>www.velvetcrest.ch</div>
  </div>

  <div class="panel panel--front">
    <div class="front-name">VELVET<br>CREST</div>
    <div class="front-services">
      Detailing &amp; Hand Wash<br>Polishing<br>Ceramic Treatment<br>Dry Ice Wash<br>Covering<br>Protection Film<br>Detailing Boutique
    </div>
    <div class="front-phone">2468 531 790</div>
  </div>
</section>

<!-- Inside spread -->
<section class="sheet sheet--inside" aria-label="Brochure inside">
  <div class="photo" style="left:0;top:0;width:161px;height:215px;background:linear-gradient(160deg,#8d9196,#55595e 55%,#2f3134)" role="img" aria-label="Photo of a foamed sports car bonnet being cleaned with a brush"></div>
  <div class="abs white-bar" style="left:163px;top:171px;width:8px;height:52px"></div>
  <div class="abs white-bar" style="left:65px;top:215px;width:106px;height:8px"></div>

  <div class="abs services-band">SERVICES:</div>

  <div class="abs service-title" style="left:282px;top:132px">DETAILING &amp; HAND WASH</div>
  <ul class="abs bullets" style="left:282px;top:162px">
    <li>Comprehensive exterior &amp; interior care</li>
    <li>Personalisation and tailored cleaning packages</li>
    <li>Decontamination</li>
    <li>Premium products</li>
    <li>Attention to detail for a perfect finish</li>
  </ul>

  <div class="abs about-title">ABOUT US</div>
  <p class="abs about-text">The ultimate destination for car care in Geneva. We provide personalized, detail-oriented services that bring out the best in your car. With our expert techniques and dedicated approach, we ensure that your car receives the utmost care and attention. Experience a place where passion meets precision and let us create an exceptional car care experience designed just for you.</p>

  <div class="abs label-box">POLISHING</div>
  <ul class="abs bullets" style="left:282px;top:323px">
    <li>Eliminates scratches, holograms</li>
    <li>Revives and protects paint</li>
    <li>Ensures lasting gloss</li>
    <li>Enhances paint life</li>
    <li>Preserves car’s value and beauty</li>
  </ul>
  <div class="abs white-bar" style="left:473px;top:254px;width:30px;height:14px"></div>
  <div class="photo" style="left:439px;top:268px;width:92px;height:131px;background:linear-gradient(170deg,#5b5f66,#2e3035 60%,#1f2024)" role="img" aria-label="Photo of a polishing machine working on car paint"></div>

  <div class="abs white-bar" style="left:80px;top:465px;width:14px;height:72px"></div>
  <div class="photo" style="left:94px;top:440px;width:172px;height:122px;background:linear-gradient(140deg,#a5a8ac,#6b6e72 50%,#3b3d40)" role="img" aria-label="Photo of a wash mitt cleaning a car wheel during ceramic treatment"></div>
  <div class="abs ceramic-box">
    <div class="service-title">CERAMIC TREATMENT</div>
    <ul class="bullets" style="margin-top:4px">
      <li>Durable paint protection</li>
      <li>Water-repellent (hydrophobic) effect</li>
      <li>Easier cleaning, enhanced shine</li>
      <li>Long-term surface safeguarding</li>
      <li>Shields against environmental impacts</li>
    </ul>
  </div>

  <div class="abs service-title grad-text" style="left:557px;top:36px">DRY ICE WASH</div>
  <ul class="abs bullets" style="left:557px;top:66px">
    <li>Innovative, waterless method</li>
    <li>Safe for all car parts</li>
    <li>Deep cleans, removes odors</li>
    <li>Allergen-free, antibacterial</li>
    <li>Gentle, effective</li>
    <li>Advanced cleaning technology</li>
  </ul>
  <div class="photo" style="left:708px;top:0;width:88px;height:188px;background:linear-gradient(180deg,#6a6d72,#3a3c40 55%,#c8782e 80%,#2a2b2e)" role="img" aria-label="Photo of an orange microfibre towel and detailing products in a studio"></div>

  <div class="abs covering-band">COVERING</div>
  <ul class="abs bullets" style="left:557px;top:220px">
    <li>Personalized vehicle styling</li>
    <li>More than 150 colours available</li>
    <li>Clean cut without using a cutter</li>
    <li>High-quality, durable materials</li>
    <li>Custom designs available</li>
  </ul>

  <div class="abs service-title grad-text" style="left:557px;top:317px">PROTECTION FILM</div>
  <ul class="abs bullets" style="left:557px;top:347px">
    <li>Invisible, durable shield</li>
    <li>Self-healing technology</li>
    <li>10-year warranty by QR VONT</li>
  </ul>

  <div class="abs service-title" style="left:557px;top:426px">DETAILING BOUTIQUE</div>
  <ul class="abs bullets" style="left:557px;top:469px">
    <li>Premium brands available</li>
    <li>Buy on site during your visit</li>
    <li>Marble Harbour, Zeb Autos, DRUP Polaro</li>
    <li>Essential for at-home car care</li>
    <li>Perfect for quick touch-ups</li>
  </ul>
</section>

</body>
</html>
```